TrueForm Nutrition

We are a nutritional coaching business who specalise in:

Weight Loss
Improved Body Composition
Personalised Meal Plans
Health & Vitality

We are in the process of developing a FriendSpace page and need a cover photo design. Our logo has already been created which we will use for the profile pic. We would like the background to be simple and include our logo as well as the 4 dot points above.

Industry/Entity Type

Business

Requirements
Must have
• Please make sure the design will upload easily to FriendSpace, specifically the cover photo and not become distorted.

```html
<!DOCTYPE html>
<html lang="en">
<head>
<meta charset="utf-8">
<title>TrueForm Nutrition – Cover</title>
<link href="https://fonts.googleapis.com/css2?family=Lobster&family=Open+Sans:wght@400;600;700&family=Raleway:ital,wght@0,300;0,600;1,400;1,700;1,800&display=swap" rel="stylesheet">
<style>
  :root {
    --stage: #333333;
    --paper: #ffffff;
    --brand-blue: #0a7bd6;
    --brand-green: #5cb314;
    --soft-blue: #9ccaf0;
    --ink-blue: #1a73cf;
    --ui-grey: #e9ebee;
    --ui-line: #d3d6db;
    --ui-text: #3b5998;
    --ui-dark: #333333;
    --guide: #8a8a8a;
  }
  html, body {
    margin: 0;
    width: 1200px;
    height: 1000px;
    overflow: hidden;
    background: var(--stage);
  }
  .canvas { position: relative; width: 1200px; height: 1000px; }
  .defs { position: absolute; width: 0; height: 0; overflow: hidden; }

  .cover {
    position: absolute;
    left: 175px;
    top: 66px;
    width: 851px;
    height: 315px;
    display: block;
  }

  .guide-label {
    position: absolute;
    font-family: "Raleway", sans-serif;
    font-style: italic;
    font-size: 13px;
    color: var(--brand-green);
    white-space: nowrap;
  }
  .guide-line { position: absolute; height: 1px; background: var(--guide); }
  .guide-line.vertical { width: 1px; height: auto; }

  .mockup-title {
    position: absolute;
    left: 338px;
    top: 485px;
    font-family: "Raleway", sans-serif;
    font-style: italic;
    font-size: 22px;
    color: var(--paper);
    white-space: nowrap;
  }

  .profile-tile {
    position: absolute;
    background: var(--paper);
    border: 4px solid var(--brand-green);
    box-sizing: border-box;
    display: flex;
    align-items: center;
    justify-content: center;
  }
  .profile-tile.standalone { left: 67px; top: 656px; width: 156px; height: 153px; }
  .profile-tile.in-page { left: 351px; top: 700px; width: 156px; height: 152px; box-shadow: 0 0 0 1px #ccc; }
  .profile-name {
    font-family: "Raleway", sans-serif;
    font-weight: 600;
    font-size: 17px;
    color: var(--ink-blue);
    text-align: center;
    line-height: 1.15;
  }

  .page-frame {
    position: absolute;
    left: 328px;
    top: 535px;
    width: 817px;
    height: 351px;
    background: var(--ui-grey);
    overflow: hidden;
  }
  .page-cover {
    position: absolute;
    left: 7px;
    top: 0;
    width: 813px;
    height: 301px;
  }
  .page-nav {
    position: absolute;
    left: 9px;
    top: 294px;
    width: 800px;
    height: 40px;
    background: var(--paper);
    border-bottom: 1px solid var(--ui-line);
    font-family: "Open Sans", sans-serif;
    font-size: 12px;
    font-weight: 700;
    color: var(--ui-text);
  }
  .page-nav .tab {
    position: absolute;
    top: 0;
    height: 40px;
    line-height: 40px;
    box-sizing: border-box;
    border-left: 1px solid var(--ui-line);
    padding: 0 15px;
    white-space: nowrap;
  }
  .page-nav .tab.active { color: var(--ui-dark); }
  .page-nav .count { font-weight: 400; font-size: 11px; color: #888; margin-left: 4px; }
  .page-nav .caret { font-size: 9px; margin-left: 4px; }
  .page-card {
    position: absolute;
    left: 9px;
    top: 347px;
    width: 303px;
    height: 20px;
    background: var(--paper);
    border: 1px solid var(--ui-line);
  }

  .page-buttons {
    position: absolute;
    top: 255px;
    height: 22px;
    display: flex;
    font-family: "Open Sans", sans-serif;
    font-size: 12px;
    font-weight: 700;
    color: var(--ui-dark);
  }
  .page-buttons .btn {
    height: 22px;
    line-height: 20px;
    box-sizing: border-box;
    padding: 0 6px;
    background: #f6f7f9;
    border: 1px solid #9197a3;
    white-space: nowrap;
  }
  .page-buttons .btn + .btn { border-left: none; }
  .star { color: #f5b400; margin-right: 3px; }
</style>
</head>
<body>
<main class="canvas">

  <svg class="defs" aria-hidden="true">
    <defs>
      <clipPath id="panel-clip">
        <polygon points="47,0 432,0 337,259 46,62"/>
      </clipPath>
      <linearGradient id="runner-tone" x1="0" y1="0" x2="0" y2="1">
        <stop offset="0" stop-color="#c99a7e"/>
        <stop offset="0.45" stop-color="#d9755f"/>
        <stop offset="1" stop-color="#4a4756"/>
      </linearGradient>
      <linearGradient id="coach-tone" x1="0" y1="0" x2="0" y2="1">
        <stop offset="0" stop-color="#f1e0c4"/>
        <stop offset="0.5" stop-color="#dfe8f0"/>
        <stop offset="1" stop-color="#4b4a5a"/>
      </linearGradient>
      <symbol id="cover-art" viewBox="0 0 851 315">
        <rect width="851" height="315" fill="var(--paper)"/>
        <polygon points="46,62 326,270 438,0 432,0 337,259" fill="var(--brand-green)"/>
        <polygon points="47,0 432,0 337,259 46,62" fill="var(--brand-blue)"/>
        <g clip-path="url(#panel-clip)">
          <rect x="212" y="0" width="150" height="245" rx="50" fill="url(#runner-tone)" opacity="0.9"
                role="img" aria-label="Photo of a fit woman measuring her waist with a tape"/>
        </g>
        <g font-family="Raleway, sans-serif" font-style="italic" font-weight="800" fill="var(--soft-blue)">
          <text x="66" y="33" font-size="27">Improved</text>
          <text x="112" y="42" font-size="10" font-weight="700">Body composition</text>
          <text x="188" y="67" font-size="21">Weight</text>
          <text x="239" y="82" font-size="15" font-weight="700">loss</text>
          <text x="130" y="101" font-size="25">Health</text>
          <text x="153" y="117" font-size="16" font-weight="700">and Vitality</text>
        </g>
        <g font-family="Raleway, sans-serif" font-style="italic" font-weight="700" font-size="14.5" fill="var(--ink-blue)" text-anchor="end">
          <text x="631" y="73">Alter body composition</text>
          <text x="631" y="87">and transform people through</text>
        </g>
        <rect x="680" y="30" width="150" height="190" rx="40" fill="url(#coach-tone)"
              role="img" aria-label="Photo of a smiling woman sitting cross-legged holding a plate of vegetables and a dumbbell"/>
        <text x="727" y="159" font-family="Raleway, sans-serif" font-weight="300" font-size="50" fill="var(--soft-blue)">&amp;</text>
        <text x="420" y="216" font-family="Lobster, cursive" font-size="136" fill="var(--brand-green)">Diet</text>
        <text x="534" y="259" font-family="Raleway, sans-serif" font-weight="300" font-size="74" fill="var(--brand-blue)" textLength="276" lengthAdjust="spacingAndGlyphs">exercise</text>
        <rect x="0" y="305" width="851" height="10" fill="var(--brand-blue)"/>
      </symbol>
    </defs>
  </svg>

  <svg class="cover" viewBox="0 0 851 315" aria-label="TrueForm Nutrition cover"><use href="#cover-art"/></svg>

  <div class="guide-line" style="left:79px; top:637px; width:34px;"></div>
  <div class="guide-label" style="left:118px; top:628px;">125x125</div>
  <div class="guide-line" style="left:182px; top:637px; width:40px;"></div>

  <aside class="profile-tile standalone" aria-label="Profile picture">
    <div class="profile-name">TrueForm<br>Nutrition</div>
  </aside>

  <div class="mockup-title">Final Result on FriendSpace</div>
  <div class="guide-line" style="left:336px; top:513px; width:339px;"></div>
  <div class="guide-label" style="left:681px; top:504px;">851x315 Perfect fit</div>
  <div class="guide-line" style="left:818px; top:513px; width:318px;"></div>
  <div class="guide-line vertical" style="left:1165px; top:535px; height:293px;"></div>

  <section class="page-frame" aria-label="Cover shown on a profile page">
    <svg class="page-cover" viewBox="0 0 851 315"><use href="#cover-art"/></svg>

    <div class="page-buttons" style="left:533px;">
      <div class="btn"><span class="star">★</span>Friends</div>
    </div>
    <div class="page-buttons" style="left:624px;">
      <div class="btn">Message</div>
      <div class="btn">Give Gift</div>
      <div class="btn">✲ <span style="color:var(--ui-text); font-size:9px;">▼</span></div>
    </div>

    <nav class="page-nav">
      <div class="tab active" style="left:189px; width:82px;">Timeline</div>
      <div class="tab" style="left:271px; width:71px;">About</div>
      <div class="tab" style="left:342px; width:108px;">Friends<span class="count">2,513</span></div>
      <div class="tab" style="left:450px; width:97px;">Photos<span class="count">111</span></div>
      <div class="tab" style="left:547px; width:79px;">More<span class="caret">▼</span></div>
      <div class="tab" style="left:626px; width:1px; padding:0;"></div>
    </nav>
    <div class="page-card"></div>
  </section>

  <aside class="profile-tile in-page" aria-label="Profile picture on page">
    <div class="profile-name">TrueForm<br>Nutrition</div>
  </aside>

</main>
</body>
</html>
```